Business Card and Stationary Design

After the successful redesign of our logo we are wanting to follow suite and create a new business card and stationary design!

New Logo is attached, information required on the business card should contain a mixture of the following but layout/arrangement is up to the designer.

Happy if the national provider number and abn are on the back, and happy for them to be smaller than the rest.

I am also happy to receive single sided or weird and wonderful designs.

Name
Title
National Provider Number 7192
ABN 53 614 289 117
Level 1, 214 Garrow Street
Brackenvale NSW 2291
Ph: 1300 587 902
Mobile: 0438 761 205
name@ironquillbuild.com.au
www.ironquillbuild.com.au

Target Market(s)

Professionals, Peers, Students, Suppliers...

Industry/Entity Type

Construction

Contact Information for Business Card

Listed in project description

Font styles to use
Other font styles liked:
• Century Gothic

Colors
0455a3
3176b5
ffffff

Requirements
Must have
• Professional Design, same color scheme as our logo
Nice to have
• Something that sets our apart from everyone else would be fantastic, open to size and shape and layout options, as long as they present professionally.
• Open to raised/embossed text, alternative materials, custom sizes, clear material
Should not have
• The color orange

```html
<!DOCTYPE html>
<html lang="en">
<head>
<meta charset="utf-8">
<title>Ironquill Build – Business Card</title>
<link rel="stylesheet" href="https://fonts.googleapis.com/css2?family=Questrial&display=swap">
<style>
  :root {
    --page-bg: #1f2022;
    --card-frost: #c7cacf;
    --card-edge: #dfe2e6;
    --brand-blue: #0455a3;
    --band-blue: #2d4f94;
    --ink-light: #ffffff;
    --ink-soft: #f1f3f6;
  }
  * { margin: 0; padding: 0; box-sizing: border-box; }
  html, body { width: 1200px; height: 800px; overflow: hidden; }
  body {
    background: var(--page-bg);
    font-family: "Questrial", "Century Gothic", sans-serif;
    position: relative;
  }
  .business-card {
    position: absolute;
    left: 100px; top: 115px;
    width: 1000px; height: 570px;
    border-radius: 34px;
    background: linear-gradient(160deg, var(--card-edge) 0%, var(--card-frost) 55%, #b9bdc3 100%);
    overflow: hidden;
  }
  .brand {
    position: absolute;
    left: 60px; top: 52px;
    display: flex; align-items: center; gap: 16px;
  }
  .brand-square {
    width: 34px; height: 34px;
    background: var(--brand-blue);
  }
  .brand-name {
    color: var(--brand-blue);
    font-size: 44px;
    line-height: 1;
  }
  .registration {
    position: absolute;
    right: 60px; top: 150px;
    text-align: right;
    color: var(--ink-soft);
    font-size: 24px;
    line-height: 1.3;
  }
  .name-band-frame {
    position: absolute;
    left: 400px; right: 0; top: 224px;
    height: 114px;
    border-top: 2px solid var(--ink-light);
    border-bottom: 2px solid var(--ink-light);
    padding: 5px 0;
  }
  .name-band {
    position: relative;
    height: 100%;
    background: var(--band-blue);
  }
  .person {
    position: absolute;
    right: 60px; top: 8px;
    text-align: right;
    color: var(--ink-light);
  }
  .person-name { font-size: 40px; line-height: 1.05; letter-spacing: 1px; }
  .person-title { font-size: 29px; line-height: 1.1; }
  .address {
    position: absolute;
    left: 60px; top: 352px;
    color: var(--ink-soft);
    font-size: 29px;
    line-height: 1.25;
  }
  .contact-list {
    position: absolute;
    right: 60px; top: 372px;
    list-style: none;
    color: var(--ink-soft);
    font-size: 29px;
    line-height: 1.25;
  }
  .contact-item {
    display: flex; justify-content: flex-end; align-items: center; gap: 16px;
  }
  .contact-icon { width: 26px; height: 26px; flex: none; }
</style>
</head>
<body>
  <div class="business-card">
    <div class="brand">
      <span class="brand-square"></span>
      <span class="brand-name">Ironquill Build</span>
    </div>

    <div class="registration">
      <p>National Provider Number 7192</p>
      <p>ABN 53 614 289 117</p>
    </div>

    <div class="name-band-frame">
      <div class="name-band">
        <div class="person">
          <p class="person-name">MAREN TOLLEY</p>
          <p class="person-title">Executive Manager</p>
        </div>
      </div>
    </div>

    <div class="address">
      <p>Level 1, 214 Garrow Street</p>
      <p>Brackenvale NSW 2291</p>
    </div>

    <ul class="contact-list">
      <li class="contact-item">1300 587 902
        <svg class="contact-icon" viewBox="0 0 24 24" aria-hidden="true"><path fill="#fff" d="M6.6 10.8a15 15 0 0 0 6.6 6.6l2.2-2.2c.3-.3.7-.4 1-.2 1.1.4 2.3.6 3.6.6.6 0 1 .4 1 1V20c0 .6-.4 1-1 1A17 17 0 0 1 3 4c0-.6.4-1 1-1h3.5c.6 0 1 .4 1 1 0 1.3.2 2.5.6 3.6.1.3 0 .7-.2 1z"/></svg>
      </li>
      <li class="contact-item">0438 761 205
        <svg class="contact-icon" viewBox="0 0 24 24" aria-hidden="true"><rect x="6" y="2" width="12" height="20" rx="2" fill="#fff"/><rect x="8" y="5" width="8" height="11" fill="#b9bdc3"/><circle cx="12" cy="19" r="1.2" fill="#b9bdc3"/></svg>
      </li>
      <li class="contact-item">name@ironquillbuild.com.au
        <svg class="contact-icon" viewBox="0 0 24 24" aria-hidden="true"><rect x="2" y="5" width="20" height="14" rx="1" fill="#fff"/><path d="M2.5 6l9.5 7 9.5-7" fill="none" stroke="#b9bdc3" stroke-width="1.5"/></svg>
      </li>
      <li class="contact-item">www.ironquillbuild.com.au
        <svg class="contact-icon" viewBox="0 0 24 24" aria-hidden="true"><circle cx="12" cy="12" r="10" fill="#fff"/><g fill="none" stroke="#b9bdc3" stroke-width="1.3"><ellipse cx="12" cy="12" rx="4.5" ry="10"/><path d="M2 12h20M4 7h16M4 17h16"/></g></svg>
      </li>
    </ul>
  </div>
</body>
</html>
```